Communication and Marketing agency needs a new presentation card

We are a group of communication and marketing agencies specialized in companies that are in the logistics and industrial sector. The head agency is TELVANO Grupo and the group consists of 4 agencies: TELVANO Media, TELVANO Digital, TELVANO Research and EnlazaPorImagen. We hace 4 offices in Spain (Madrid, Barcelona, Valencia and Murcia). We are looking for a clean and attractive design that transmits our experience, brand presence in the market and knowledge to those who receive the card.It has to maintain the colors of the logo that is attached.
Target Market(s)
logistics and industrial sector
Marketing department
Clean and attractive design

```html
<!DOCTYPE html>
<html lang="en">
<head>
<meta charset="utf-8">
<title>TELVANO Grupo – Business Card</title>
<link rel="stylesheet" href="https://fonts.googleapis.com/css2?family=Montserrat:wght@300;400;700&display=swap">
<style>
  :root {
    --backdrop: #3f4043;
    --card-grey: #58585a;
    --band-grey: #545150;
    --brand-red: #b41f2a;
    --paper: #ffffff;
    --ink-light: #d9d9d9;
  }
  * { box-sizing: border-box; margin: 0; padding: 0; }
  html, body {
    width: 1200px; height: 960px; overflow: hidden;
    background: var(--backdrop);
    font-family: "Montserrat", sans-serif;
  }
  .canvas {
    position: relative; width: 1200px; height: 960px;
    display: flex; flex-direction: column; align-items: center;
    justify-content: center; gap: 48px;
  }
  .card {
    position: relative; width: 720px; height: 412px; overflow: hidden;
    box-shadow: 0 10px 30px rgba(0,0,0,.35);
  }

  /* Back side */
  .card--back {
    background: var(--card-grey);
    display: grid;
    grid-template-columns: minmax(0, 1fr) minmax(0, 1fr);
    grid-template-rows: 1fr 1fr;
    padding: 110px 50px; column-gap: 30px; row-gap: 24px;
  }
  .agency-name {
    color: var(--paper); font-weight: 300; font-size: 26px;
    letter-spacing: .5px; line-height: 1;
    display: flex; align-items: center; justify-content: center;
    white-space: nowrap; min-width: 0;
  }

  /* Front side */
  .card--front { background: var(--paper); }
  .brand {
    position: absolute; top: 92px; left: 0; width: 100%;
    text-align: center; color: var(--brand-red);
    font-weight: 300; font-size: 54px; letter-spacing: 2px; line-height: 1;
    white-space: nowrap;
  }
  .info-band {
    position: absolute; top: 232px; left: 0; width: 100%; height: 112px;
    background: var(--band-grey);
  }
  .person {
    position: absolute; right: 388px; top: 32px; text-align: right; color: var(--paper);
  }
  .person__name { font-weight: 700; font-size: 21px; line-height: 1.2; }
  .person__title { font-weight: 300; font-size: 16px; color: var(--ink-light); margin-top: 2px; }
  .divider {
    position: absolute; left: 352px; top: 18px; width: 1px; height: 76px;
    background: var(--ink-light);
  }
  .contact-list {
    position: absolute; left: 374px; top: 23px; list-style: none;
    color: var(--paper); font-weight: 300; font-size: 15px;
  }
  .contact-list li { display: flex; align-items: center; gap: 10px; height: 22px; white-space: nowrap; }
  .contact-list svg { width: 15px; height: 15px; fill: var(--paper); flex: none; }
  .address-band {
    position: absolute; left: 0; bottom: 0; width: 100%; height: 68px;
    background: var(--brand-red); border-top: 6px solid var(--paper);
    display: flex; align-items: center; justify-content: center;
    color: var(--paper); font-weight: 400; font-size: 18px; letter-spacing: .5px;
    white-space: nowrap;
  }
</style>
</head>
<body>
<main class="canvas">
  <section class="card card--back" aria-label="Card back">
    <span class="agency-name">TELVANO Media</span>
    <span class="agency-name">TELVANO Digital</span>
    <span class="agency-name">TELVANO Research</span>
    <span class="agency-name">EnlazaPorImagen</span>
  </section>

  <section class="card card--front" aria-label="Card front">
    <h1 class="brand">TELVANO Grupo</h1>
    <div class="info-band">
      <div class="person">
        <p class="person__name">Your Name</p>
        <p class="person__title">Your Title</p>
      </div>
      <span class="divider"></span>
      <ul class="contact-list">
        <li>
          <svg viewBox="0 0 24 24" aria-hidden="true"><path d="M6.6 10.8a15.1 15.1 0 0 0 6.6 6.6l2.2-2.2a1 1 0 0 1 1-.25 11.4 11.4 0 0 0 3.6.57 1 1 0 0 1 1 1V20a1 1 0 0 1-1 1A17 17 0 0 1 3 4a1 1 0 0 1 1-1h3.5a1 1 0 0 1 1 1c0 1.25.2 2.450.57 3.57a1 1 0 0 1-.25 1z"/></svg>
          123-456-2100
        </li>
        <li>
          <svg viewBox="0 0 24 24" aria-hidden="true"><path d="M2 5h20v14H2zm2 2v.5l8 5 8-5V7zm0 2.8V17h16V9.8l-8 5z"/></svg>
          youremail@mailbox.com
        </li>
        <li>
          <svg viewBox="0 0 24 24" aria-hidden="true"><path d="M12 2a10 10 0 1 0 0 20 10 10 0 0 0 0-20zm0 2a8 8 0 0 1 5.3 2H6.7A8 8 0 0 1 12 4zM4.3 10h4.2v4H4.3a8 8 0 0 1 0-4zm6.2 0h3v4h-3zm5 0h4.2a8 8 0 0 1 0 4h-4.2zM6.7 18h10.6a8 8 0 0 1-10.6 0z"/></svg>
          www.yourwebsite.com
        </li>
      </ul>
    </div>
    <div class="address-band">Your address, city, state, ZIP 0000</div>
  </section>
</main>
</body>
</html>
```